Pool Screen Enclosure Building a Career Boot Camp!

Looking to Host a Boot Camp for people looking for a career or looking to change careers. We Design, Manufacture and Install Custom Pool Screen Enclosures. We have a training program to allow Non Experienced motivated people the chance at a great career that will provide a great living for them and their family. This will be a paid boot camp, week long, we provide all the initial training for them to make a transition into our business. This will be 5 days of training with a guaranteed job to start the following Monday.... This is good for both someone with no construction experience or someone with construction experience that wants to upgrade their current job.
Paid Boot Camp
transition to a full time job with great pay
Benefits include Health Insurance, Dental and Vision, 401K, we provide the tools and training.

```html
<!DOCTYPE html>
<html lang="en">
<head>
<meta charset="utf-8">
<title>Pool Screen Enclosure Career Boot Camp</title>
<link rel="stylesheet" href="https://fonts.googleapis.com/css2?family=Lato:ital,wght@0,400;0,700;0,900;1,400&family=Fira+Sans:ital,wght@1,500&display=swap">
<style>
  :root {
    --green: #6cbf45;
    --black: #0b0b0b;
    --frame: #3a3a3a;
    --ink: #111111;
    --body: #2b2b2b;
    --white: #ffffff;
    --tagline: #c9c27a;
  }
  * { margin: 0; padding: 0; box-sizing: border-box; }
  html, body { width: 972px; height: 1200px; overflow: hidden; background: var(--white); }
  .flyer { position: relative; width: 972px; height: 1200px; background: var(--white); font-family: "Lato", sans-serif; color: var(--ink); overflow: hidden; }

  .header-bg { position: absolute; left: 0; top: 0; width: 972px; height: 142px; }
  .brand-dot { position: absolute; left: 68px; top: 58px; width: 62px; height: 62px; border-radius: 50%; background: var(--green); }
  .brand-name { position: absolute; left: 172px; top: 54px; font-weight: 900; font-size: 44px; line-height: 48px; color: var(--green); letter-spacing: -0.5px; white-space: nowrap; }
  .brand-tagline { position: absolute; left: 206px; top: 108px; font-style: italic; font-size: 17px; line-height: 20px; color: var(--tagline); white-space: nowrap; }
  .contact { position: absolute; right: 40px; top: 62px; text-align: right; color: var(--ink); }
  .contact-phone { font-weight: 900; font-size: 35px; line-height: 36px; letter-spacing: -0.5px; }
  .contact-email { font-size: 17px; line-height: 20px; margin-top: 1px; }

  .content-frame { position: absolute; left: 35px; top: 193px; width: 563px; height: 630px; border-left: 4px solid var(--frame); border-top: 4px solid var(--frame); }

  .headline { position: absolute; left: 30px; top: 232px; width: 334px; text-align: right; font-weight: 900; font-size: 46px; line-height: 50px; letter-spacing: -0.8px; white-space: nowrap; }
  .headline-rule { position: absolute; left: 371px; top: 238px; width: 3px; height: 92px; background: var(--green); }
  .subhead { position: absolute; left: 381px; top: 236px; font-weight: 700; font-size: 31px; line-height: 32px; white-space: nowrap; }

  .pay-bar { position: absolute; left: 59px; top: 355px; width: 543px; height: 36px; background: var(--green); font-weight: 900; font-size: 20.5px; line-height: 36px; text-align: center; white-space: nowrap; }

  .benefits { position: absolute; left: 48px; top: 424px; width: 564px; text-align: center; font-size: 21.5px; line-height: 26px; }
  .benefits-title { font-weight: 900; }

  .about { position: absolute; left: 52px; width: 560px; text-align: center; font-size: 14px; line-height: 18.6px; color: var(--body); }
  .about-1 { top: 537px; }
  .about-2 { top: 610px; }
  .about-3 { top: 702px; }

  .green-band { position: absolute; left: 0; top: 808px; width: 972px; height: 28px; background: var(--green); }
  .hero-photo { position: absolute; left: 0; top: 822px; width: 972px; height: 378px; background: linear-gradient(180deg, #3b3a36 0%, #9ea3a6 14%, #c4c8ca 32%, #7e7f79 58%, #58614f 72%, #6f9fa6 86%, #3f7f8c 100%); }
  .address-bar { position: absolute; left: 0; top: 1095px; width: 636px; height: 52px; background: rgba(20,20,20,0.82); color: var(--white); font-family: "Fira Sans", sans-serif; font-style: italic; font-weight: 500; font-size: 26px; line-height: 52px; padding-left: 74px; white-space: nowrap; }

  .photo { position: absolute; left: 647px; width: 293px; border: 5px solid var(--white); box-shadow: 4px 5px 10px rgba(0,0,0,0.35); }
  .photo-crew { top: 172px; height: 317px; background: linear-gradient(170deg, #b8ad98 0%, #a7a39a 30%, #8c8a84 60%, #6a6862 100%); }
  .photo-frame { top: 503px; height: 318px; background: linear-gradient(180deg, #2a2b2c 0%, #b9c1c8 22%, #dfe4e8 45%, #7b8577 70%, #8f8a80 100%); }
  .photo-roof { top: 834px; height: 319px; background: linear-gradient(180deg, #5f8fc9 0%, #a9c4e2 35%, #d9dfe3 55%, #9d9588 80%, #8a8a86 100%); }
</style>
</head>
<body>
<div class="flyer">
  <svg class="header-bg" viewBox="0 0 972 142" aria-hidden="true">
    <rect x="0" y="0" width="972" height="134" fill="var(--green)"/>
    <polygon points="0,40 692,40 624,142 0,142" fill="var(--black)"/>
  </svg>
  <span class="brand-dot"></span>
  <span class="brand-name">Harbor Screen Works</span>
  <span class="brand-tagline">“Screened in, built to last”</span>
  <div class="contact">
    <div class="contact-phone">555-010-4477</div>
    <div class="contact-email">Admin@harborscreenworks.com</div>
  </div>

  <div class="content-frame"></div>
  <h1 class="headline">POOL SCREEN<br>ENCLOSURE</h1>
  <div class="headline-rule"></div>
  <h2 class="subhead">BUILDING A<br>CAREER BOOT<br>CAMP!</h2>

  <div class="pay-bar">TRANSITION TO A FULL TIME JOB WITH GREAT PAY</div>

  <div class="benefits">
    <div class="benefits-title">BENEFITS INCLUDE:</div>
    <div>• Health Insurance • Dental and Vision• 401K</div>
    <div>we provide the tools and training.</div>
  </div>

  <p class="about about-1">We Design, Manufacture and Install Custom Pool Screen Enclosures. We have a training program to allow Non Experienced motivated people the chance at a great career that will provide a great living for them and their family.</p>
  <p class="about about-2">This will be a paid boot camp, week long, we provide all the initial training for them to make a transition into our business. This will be 5 days of training with a guaranteed job to start the following Monday....</p>
  <p class="about about-3">This is good for both someone with no construction experience or someone with construction experience that wants to upgrade their current job.</p>

  <div class="green-band"></div>
  <div class="hero-photo" role="img" aria-label="Finished pool screen enclosure over a lit pool at dusk, overlooking a lake"></div>
  <div class="address-bar">1420 Palm Grove Avenue, Fort Pierce FL 34950</div>

  <div class="photo photo-crew" role="img" aria-label="Crew kneeling on a concrete slab reviewing enclosure plans"></div>
  <div class="photo photo-frame" role="img" aria-label="Installer on a ladder fitting screen panels to an enclosure frame"></div>
  <div class="photo photo-roof" role="img" aria-label="Two installers placing screen on a white enclosure roof frame"></div>
</div>
</body>
</html>
```